Brightfield Steel Depot (Metal Roofing Manufacturing and Supply) needs a billboard design

We need a billboard design for for our metal roofing manufacturing company in Sarasota FL, Brightfield Steel Depot Inc. You can visit our website www.brightfieldsteeldepot-example.com for more info about our company. We located are off Exit 210 on I 75- 482 Harrowgate Rd. Sarasota 34290
The billboard will be on I75 north of our office

I have a design that I am interested in but waiting on minor corrections from designer

```html
<!DOCTYPE html>
<html lang="en">
<head>
<meta charset="utf-8">
<title>Brightfield Steel Depot Billboard</title>
<link href="https://fonts.googleapis.com/css2?family=Montserrat:wght@500;600;700;800&display=swap" rel="stylesheet">
<style>
  :root {
    --stage: #3c3c3c;
    --navy: #163466;
    --royal: #1f4fae;
    --ink: #111a2b;
    --sun: #f7b500;
    --paper: #ffffff;
    --paper-shade: #eef0f3;
    --roof-deep: #1d3466;
    --roof-mid: #40558a;
    --timber: #c8915a;
  }
  * { margin: 0; padding: 0; box-sizing: border-box; }
  html, body { width: 972px; height: 1200px; overflow: hidden; background: var(--stage); }
  body { font-family: "Montserrat", sans-serif; position: relative; }

  .billboard {
    position: absolute; left: 36px; top: 375px;
    width: 900px; height: 450px; overflow: hidden;
    box-shadow: 0 24px 30px rgba(0,0,0,0.45);
  }
  .billboard-art { position: absolute; inset: 0; }

  .brand { position: absolute; right: 30px; top: 44px; display: flex; align-items: center; gap: 12px; }
  .brand-mark { width: 16px; height: 16px; background: var(--sun); }
  .brand-name { font-weight: 600; font-size: 34px; color: var(--royal); letter-spacing: -0.3px; }

  .tagline {
    position: absolute; right: 28px; top: 110px; text-align: right;
    font-weight: 800; font-size: 26px; line-height: 34px; color: var(--ink); letter-spacing: 0.3px;
  }

  .services { position: absolute; right: 24px; top: 190px; display: flex; gap: 26px; }
  .service { width: 110px; text-align: center; }
  .service-icon {
    width: 70px; height: 70px; margin: 0 auto 10px; border-radius: 50%;
    background: var(--navy); border: 3px solid var(--paper); box-shadow: 0 0 0 2px var(--navy);
    display: flex; align-items: center; justify-content: center;
  }
  .service-label { font-weight: 500; font-size: 17px; line-height: 21px; color: var(--ink); }

  .contact { position: absolute; right: 24px; top: 338px; color: var(--paper); text-align: right; }
  .contact-row { display: flex; align-items: center; justify-content: flex-end; gap: 12px; }
  .contact-phone { font-weight: 800; font-size: 27px; line-height: 36px; }
  .contact-web { font-weight: 500; font-size: 17px; line-height: 30px; }
  .contact-address { font-weight: 500; font-size: 15.5px; line-height: 28px; }
</style>
</head>
<body>
  <div class="billboard">
    <svg class="billboard-art" viewBox="0 0 900 450" width="900" height="450">
      <defs>
        <linearGradient id="roofPhoto" x1="0" y1="0" x2="0.4" y2="1">
          <stop offset="0" stop-color="#7c6e5c"/>
          <stop offset="0.35" stop-color="var(--timber)"/>
          <stop offset="0.55" stop-color="var(--roof-mid)"/>
          <stop offset="1" stop-color="var(--roof-deep)"/>
        </linearGradient>
        <linearGradient id="panelShade" x1="0" y1="0" x2="1" y2="0">
          <stop offset="0" stop-color="var(--paper-shade)"/>
          <stop offset="1" stop-color="var(--paper)"/>
        </linearGradient>
      </defs>
      <rect class="panel" width="900" height="450" fill="url(#panelShade)"/>
      <rect class="contact-band" x="400" y="327" width="500" height="123" fill="var(--navy)"/>
      <polygon class="chevron-sun" points="0,0 334,0 529,317 429,450 0,450" fill="var(--sun)"/>
      <polygon class="chevron-gap" points="0,0 314,0 509,317 409,450 0,450" fill="var(--paper)"/>
      <polygon class="photo-area" role="img" aria-label="Photo of a roofer installing blue metal roof panels over wooden battens"
               points="0,0 300,0 495,317 395,450 0,450" fill="url(#roofPhoto)"/>
    </svg>

    <div class="brand">
      <span class="brand-mark"></span>
      <span class="brand-name">Brightfield Steel Depot</span>
    </div>

    <div class="tagline">FLORIDA'S PREMIER METAL<br>ROOF MANUFACTURER</div>

    <div class="services">
      <div class="service">
        <div class="service-icon">
          <svg width="30" height="30" viewBox="0 0 30 30"><rect x="6" y="5" width="18" height="21" fill="#fff"/><rect x="10" y="9" width="3" height="3" fill="var(--navy)"/><rect x="17" y="9" width="3" height="3" fill="var(--navy)"/><rect x="10" y="15" width="3" height="3" fill="var(--navy)"/><rect x="17" y="15" width="3" height="3" fill="var(--navy)"/><rect x="13" y="20" width="4" height="6" fill="var(--navy)"/></svg>
        </div>
        <div class="service-label">Wholesale<br>Supplies</div>
      </div>
      <div class="service">
        <div class="service-icon">
          <svg width="30" height="30" viewBox="0 0 30 30"><g fill="none" stroke="#fff" stroke-width="3"><path d="M5 10 L25 10"/><path d="M5 16 L25 16"/><path d="M5 22 L25 22"/></g></svg>
        </div>
        <div class="service-label">Metal Panel<br>Profiles</div>
      </div>
      <div class="service">
        <div class="service-icon">
          <svg width="30" height="30" viewBox="0 0 30 30"><rect x="5" y="5" width="20" height="20" fill="none" stroke="#fff" stroke-width="2.5"/><path d="M9 21 L21 9" stroke="#fff" stroke-width="3"/></svg>
        </div>
        <div class="service-label">Builders<br>Toolkit</div>
      </div>
    </div>

    <div class="contact">
      <div class="contact-row contact-phone">
        <svg width="22" height="22" viewBox="0 0 22 22"><circle cx="11" cy="11" r="10" fill="#fff"/><path d="M7 6 L9.5 6 L10.5 9 L9 10.2 Q10.5 12.8 12 13.5 L13.2 12 L16 13 L16 15.5 Q10.5 16 6.5 10 Q6.2 7.5 7 6 Z" fill="var(--navy)"/></svg>
        <span>941-555-0182</span>
      </div>
      <div class="contact-row contact-web">
        <svg width="20" height="20" viewBox="0 0 20 20"><circle cx="10" cy="10" r="9" fill="#fff"/><g fill="none" stroke="var(--navy)" stroke-width="1.3"><circle cx="10" cy="10" r="5.5"/><ellipse cx="10" cy="10" rx="2.3" ry="5.5"/><path d="M4.5 10 H15.5"/></g></svg>
        <span>www.brightfieldsteeldepot-example.com</span>
      </div>
      <div class="contact-row contact-address">
        <svg width="18" height="22" viewBox="0 0 18 22"><path d="M9 1 C4.5 1 1.5 4.3 1.5 8.3 C1.5 13.5 9 21 9 21 C9 21 16.5 13.5 16.5 8.3 C16.5 4.3 13.5 1 9 1 Z" fill="#fff"/><circle cx="9" cy="8.3" r="3" fill="var(--navy)"/></svg>
        <span>482 Harrowgate Road Sarasota, Fl 34290</span>
      </div>
    </div>
  </div>
</body>
</html>
```